Birchgate Foot & Ankle Centers Trifold Brochure

I would like a trifold brochure for a podiatry office. I saw this example on the Artbazaar website and really like it (Stride Haven (Podiatry and Physiotherapy) Clinical Brochure). I would like something very similar. We are a foot and ankle specialist office. I like the blue color in the example above. I would like our 4 doctor pictures with names on the back. I would like our 3 locations listed with the addresses and phone numbers. Our doctor pictures and locations are on our website birchgatefootcare.example. I have uploaded examples of treatment options and they are all about the same as the brochure picture that I uploaded. Heel pain, ingrown toenails, ugly toenails, arthritis are some of the main things we treat but we treat all foot and ankle problems. Our slogan where the example has says "Your feet carry you through life..." Our slogan for that area could be "Improving lives one foot at a time"

Target Market(s)

People who work on their feet

Industry/Entity Type

Podiatrist: Foot and Ankle Specialists

Font styles to use
Other font styles liked:
• I uploaded some foot pictures just as examples. They do not have to be used.

Colors
0054AA
0677BA
7BADD7
CADEEF
E8F1F8
00AB8E
00BBA5
67D7C9
C6EFE9
E9F9F6

Requirements
Must have
• Our 4 doctor pictures/names. List of 3 locations with address and phone numbers (All is on website birchgatefootcare.example
Nice to have
• Something similar maybe to this Artbazaar design: Stride Haven (Podiatry and Physiotherapy) Clinical Brochure)
Should not have
• Surgical pictures. Patients think they are gross

```html
<!DOCTYPE html>
<html lang="en">
<head>
<meta charset="utf-8">
<title>Birchgate Foot &amp; Ankle Centers – Trifold Inside Spread</title>
<link href="https://fonts.googleapis.com/css2?family=Montserrat:wght@600;700&family=Source+Sans+3:wght@400;600;700&display=swap" rel="stylesheet">
<style>
  :root{
    --blue-deep:#0054AA;
    --blue-mid:#0677BA;
    --blue-soft:#7BADD7;
    --blue-pale:#CADEEF;
    --blue-mist:#E8F1F8;
    --teal:#00AB8E;
    --teal-bright:#00BBA5;
    --teal-soft:#67D7C9;
    --page-bg:#ebeceb;
    --card-line:#5b8fd0;
  }
  *{margin:0;padding:0;box-sizing:border-box}
  html,body{width:1200px;height:1200px;overflow:hidden;background:var(--page-bg)}
  .spread{
    position:absolute;left:99px;top:246px;width:1612px;height:1140px;
    transform:scale(0.6211);transform-origin:0 0;overflow:hidden;
    font-family:"Source Sans 3",sans-serif;
  }
  .panel{position:absolute;top:0;width:537px;height:1140px}
  .panel--left{left:0;background:linear-gradient(90deg,#eaf1f9 0%,#dfe9f5 75%,#d4e3f2 100%)}
  .panel--middle{left:537px;background:linear-gradient(90deg,#eef4fa 0%,#e2ecf7 70%,#d2e1f1 100%)}
  .panel--right{left:1074px;background:linear-gradient(90deg,#eef4fa 0%,#e3edf8 100%)}
  .bands{position:absolute;left:0;top:0;width:1612px;height:1140px}

  .card{position:absolute;width:484px}
  .card__tab{
    width:max-content;min-width:324px;height:64px;border-radius:9px 9px 0 0;
    background:linear-gradient(90deg,var(--blue-deep) 0%,#0a5fb4 70%,#2a78c4 100%);
    color:#fff;font-family:"Montserrat",sans-serif;font-weight:600;font-size:19.5px;
    line-height:21px;padding:0 18px 0 27px;display:flex;align-items:center;
    white-space:nowrap;
  }
  .card__box{
    border:2px solid var(--card-line);border-radius:0 9px 9px 9px;
    background:linear-gradient(90deg,rgba(255,255,255,.97) 0%,rgba(236,243,251,.9) 100%);
    padding:11px 16px 10px 24px;
  }
  .grad{
    background:linear-gradient(90deg,var(--blue-deep) 0%,var(--blue-mid) 50%,#1ea598 100%);
    -webkit-background-clip:text;background-clip:text;color:transparent;
  }
  .card__text{font-size:15px;line-height:16.8px;letter-spacing:-0.1px}
  .cols{display:grid;grid-template-columns:243px 1fr;margin-top:7px}
  .cols ul{list-style:none}
  .cols li{
    position:relative;padding-left:17px;font-weight:700;font-size:15px;line-height:19px;
  }
  .cols li::before{
    content:"";position:absolute;left:0;top:6px;width:9px;height:9px;border-radius:50%;
    background:var(--teal);
  }
</style>
</head>
<body>
<div class="spread">
  <div class="panel panel--left"></div>
  <div class="panel panel--middle"></div>
  <div class="panel panel--right"></div>

  <svg class="bands" viewBox="0 0 1612 1140">
    <defs>
      <linearGradient id="tealBand" x1="0" x2="1" y1="0" y2="0">
        <stop offset="0" stop-color="#00684f"/>
        <stop offset=".4" stop-color="#00a184"/>
        <stop offset="1" stop-color="#00AB8E"/>
      </linearGradient>
      <linearGradient id="blueBand" x1="0" x2="1">
        <stop offset="0" stop-color="#7BADD7"/>
        <stop offset=".6" stop-color="#0677BA"/>
        <stop offset="1" stop-color="#0054AA"/>
      </linearGradient>
      <linearGradient id="photoLeft" x1="0" y1="0" x2="0" y2="1">
        <stop offset="0" stop-color="#f4f1ee"/>
        <stop offset="1" stop-color="#eadcd0"/>
      </linearGradient>
      <linearGradient id="photoRoom" x1="0" y1="0" x2="0" y2="1">
        <stop offset="0" stop-color="#a9a9a3"/>
        <stop offset=".45" stop-color="#8d8c7a"/>
        <stop offset=".7" stop-color="#4a6a96"/>
        <stop offset="1" stop-color="#a66c3e"/>
      </linearGradient>
      <linearGradient id="photoFeet" x1="0" y1="0" x2="1" y2="1">
        <stop offset="0" stop-color="#e9e3df"/>
        <stop offset=".45" stop-color="#e2b59c"/>
        <stop offset="1" stop-color="#f1eeec"/>
      </linearGradient>
    </defs>
    <polygon points="0,1008 537,905 1074,760 1612,520 1612,560 1074,772 537,920 0,1020" fill="url(#blueBand)"/>
    <polygon points="0,1020 537,920 1074,772 1612,560 1612,660 1074,850 537,990 0,1040" fill="url(#tealBand)"/>
    <polygon points="0,1040 537,990 1074,850 1612,660 1612,690 1074,866 537,1000 0,1046" fill="#CADEEF"/>
    <polygon role="img" aria-label="Soft photo of a bare foot resting on a light floor" points="0,1046 537,1000 537,1140 0,1140" fill="url(#photoLeft)"/>
    <polygon role="img" aria-label="Photo of a clinic exam room with a blue treatment chair and wooden floor" points="537,1000 1074,866 1074,1140 537,1140" fill="url(#photoRoom)"/>
    <polygon role="img" aria-label="Photo of a podiatrist in gloves examining a patient's feet" points="1074,866 1612,690 1612,1140 1074,1140" fill="url(#photoFeet)"/>
  </svg>

  <!-- Left panel -->
  <section class="card" style="left:26px;top:29px">
    <h2 class="card__tab">Find Arthritis Pain Relief<br>&amp; Restore Your Mobility</h2>
    <div class="card__box">
      <p class="card__text grad">Do you have pain or stiffness in your joints? If yes, you may have arthritis and need the help from our podiatrists. Although there are more than 100 forms of arthritis, there are two main types that affect the feet- osteoarthritis and rheumatoid arthritis. Both of these forms of arthritis can cause severe pain and deformity if not properly treated.</p>
      <div class="cols">
        <ul><li class="grad">Osteoarthritis</li><li class="grad">Rheumatoid arthritis</li></ul>
        <ul><li class="grad">Gout Arthritis</li><li class="grad">Psoriatic arthritis</li></ul>
      </div>
    </div>
  </section>

  <section class="card" style="left:26px;top:287px">
    <h2 class="card__tab">Best Bunion Treatment</h2>
    <div class="card__box">
      <p class="card__text grad">Your feet bear the brunt of your weight, which makes sense why an overwhelming 77% of Americans suffer from foot pain. If it’s serious enough, it can have a significant impact on your daily life, even if you’re not very active. One of the things that might be causing you pain is a bunion.</p>
      <div class="cols">
        <ul><li class="grad">Resting your feet</li><li class="grad">Custom orthotics</li><li class="grad">Changing shoes</li><li class="grad">Padding the bunion</li></ul>
        <ul><li class="grad">Icing</li><li class="grad">Anti-inflammatory medication</li><li class="grad">Cortisone injections (Steroid injections)</li></ul>
      </div>
    </div>
  </section>

  <section class="card" style="left:26px;top:586px">
    <h2 class="card__tab">Heel Pain Relief</h2>
    <div class="card__box">
      <p class="card__text grad">We specialize in heel pain. Plantar fasciitis (heel pain) is pain in the bottom of the heel. This is the most common problem we see and we treat it about 10 times a day. Though plantar fasciitis is the most common condition associated with heel pain, it is possible your pain could be from something else.<br>Our goal is to diagnose and treat your condition quickly and accurately and provide you with the heel pain relief you are looking for. There’s nothing normal about heel pain so we’re here to help you heal your pain and get back on your feet as soon as possible.</p>
      <div class="cols">
        <ul><li class="grad">Heel spurs</li><li class="grad">Bursitis</li></ul>
        <ul><li class="grad">Achilles tendinitis</li><li class="grad">Bone bruise</li></ul>
      </div>
    </div>
  </section>

  <section class="card" style="left:26px;top:894px">
    <h2 class="card__tab">Best Ingrown Toenail<br>Doctors</h2>
    <div class="card__box">
      <p class="card__text grad">An ingrown toenail occurs when the edge of the toenail grows into the skin. This most commonly happens on the big toenails, but any toe can be affected. An ingrown toenail can get infected. Once the skin is pierced by the toenail, infection may soon follow.</p>
      <div class="cols">
        <ul><li class="grad">Incorrect toenail trimming</li><li class="grad">Genetics</li><li class="grad">Tight shoes</li></ul>
        <ul><li class="grad">Trauma</li><li class="grad">Poor pedicurist</li></ul>
      </div>
    </div>
  </section>

  <!-- Middle panel -->
  <section class="card" style="left:563px;top:29px">
    <h2 class="card__tab">Toenail Fungus<br>Doctors</h2>
    <div class="card__box">
      <p class="card__text grad">Toenail fungus, also known as Onychomycosis, affects more than 1 in every 6 Americans. It is a common fungus and athlete’s foot is caused by the same type of fungus, known as a Dermatophyte. This fungus is contagious and usually begins as a small white spot under your nail.</p>
      <div class="cols">
        <ul><li class="grad">Oral antifungal pill</li><li class="grad">Topical nail polish</li></ul>
        <ul><li class="grad">Nail removal</li></ul>
      </div>
    </div>
  </section>

  <section class="card" style="left:563px;top:270px">
    <h2 class="card__tab">Sports Injuries Care</h2>
    <div class="card__box">
      <p class="card__text grad">Sports injuries are one of the most common reasons that patients see the foot specialist at Birchgate Foot &amp; Ankle Centers. Since the feet and ankles are the foundation for almost all sports, this is not surprising.</p>
      <div class="cols">
        <ul><li class="grad">Ankle or foot Sprains</li><li class="grad">Ankle or foot Fractures</li><li class="grad">Plantar fasciitis or other types of heel pain</li></ul>
        <ul><li class="grad">Ingrown toenails</li><li class="grad">Ball of your foot pain</li><li class="grad">Calluses and/or blisters</li><li class="grad">Achilles tendonitis</li></ul>
      </div>
    </div>
  </section>

  <section class="card" style="left:563px;top:516px">
    <h2 class="card__tab">Expert Gout Relief</h2>
    <div class="card__box">
      <p class="card__text grad">Gout is actually a form of inflammatory arthritis that can occur if you have too much uric acid in your blood. Uric acid crystals are a normal blood by-product that is removed by the body in urine. If the concentration of uric acid builds up in the blood, these tiny crystals can enter into the joint, causing inflammation, swelling and severe pain. If not properly treated, this can lead to long-term joint damage.</p>
    </div>
  </section>

  <section class="card" style="left:563px;top:729px">
    <h2 class="card__tab">Diabetes Foot Care</h2>
    <div class="card__box">
      <p class="card__text grad">Over 18 million Americans are affected by diabetes and many suffer from complications related to this disease. Our award-winning podiatrists and their team at Birchgate Foot and Ankle Centers offer our patients the most advanced diabetic foot care in Westbrook, Pinehurst &amp; Corley. Our goal is to restore you to a pain-free, mobile life while providing the most advanced diabetic foot care available anywhere.</p>
    </div>
  </section>

  <!-- Right panel -->
  <section class="card" style="left:1100px;top:29px">
    <h2 class="card__tab">Specialized Wound<br>Treatment &amp; Healing</h2>
    <div class="card__box">
      <p class="card__text grad">Your award-winning podiatrists and surgeons at Birchgate Foot &amp; Ankle Centers are foot wound care specialists. With over 30 years of combined experience in treating diabetic ulcers, we are the referral of choice for doctors in Alder and Marlow counties.<br>Your podiatrists at Birchgate Foot &amp; Ankle Centers have simple in-office tests for both peripheral neuropathy and vascular disease. These tests are quick, painless, and extremely accurate.</p>
    </div>
  </section>

  <section class="card" style="left:1100px;top:260px">
    <h2 class="card__tab">Flat Feet Specialists</h2>
    <div class="card__box">
      <p class="card__text grad">Are you one of the many people who have flat feet or fallen arches? Does your child have flat feet? If so, you’re in the right place.<br>Living with flat feet can make simple tasks like walking suddenly become a painful challenge. Flat feet can also be the cause of your hip or back problems!</p>
    </div>
  </section>

  <section class="card" style="left:1100px;top:457px">
    <h2 class="card__tab">Custom Foot Orthotics</h2>
    <div class="card__box">
      <p class="card__text grad">Custom foot orthotics help prevent and relieve many different types of foot problems. They can be helpful for children’s feet and even help professional athletes perform better. These prescription shoe inserts take many hours to make and should not to be confused with the so-called “custom orthotics” that you can get at your local superstore.</p>
    </div>
  </section>

  <section class="card" style="left:1100px;top:670px">
    <h2 class="card__tab">Advanced Foot &amp; Ankle<br>Surgery</h2>
    <div class="card__box">
      <p class="card__text grad">If you’re living with a painful foot problem and it is affecting your lifestyle, foot surgery may be a viable option for you. The podiatrists at Birchgate Foot &amp; Ankle Centers have decades of experience performing the most advanced foot and ankle procedures. From simple surgery on the toes to more complex reconstructive foot surgeries, your foot specialists have the expertise to help relieve your pain so that you can have a normal, healthy lifestyle.</p>
    </div>
  </section>
</div>
</body>
</html>
```